Web Page Header (Header Only)

Our company would like to develop a new website header look for our business webpage theme. This header needs to look fantastic and add value to the overall professional appearance of our business and website design. We would like to incorporate into the design concept our company logo and use the slogan “Providing Effect Project Controls and Management Solutions” It would be great to promote our businesses global presence in the website header design concept.

For you to understand our business branding, images of our business cards, company brochure and Circlepage page have been attached to this project. A PDF file of our company logo is also attached, our website address is www.brightlanepartners.com Please read the attached webpage header PDF document attached to this project as it will you assist with your design concept. Contained within the PDF is also an example of a webpage header design.

The graphic design work needs to done in Photoshop as our business utilizes CS6. The winning design concept will be integrated into our webpage theme using our original website developer. The graphics will need to fit the dimensions for our webpage header area for easy integration.
Updates

It would be great to promote our busineses global presence in the website header design concept

Project Deadline Extended
Reason: Some designers needed more time

Industry/Entity Type

Graphic Design

Requirements
Must have
• The webpage header design must be elegant, professional,reflect a market leader and be easily integrate into the webpage design.

```html
<!DOCTYPE html>
<html lang="en">
<head>
<meta charset="utf-8">
<title>Brightlane Partners</title>
<link rel="stylesheet" href="https://fonts.googleapis.com/css2?family=Open+Sans:wght@400;600;700;800&display=swap">
<style>
  :root {
    --red: #d3202a;
    --red-deep: #b3141c;
    --ink: #1a1a1a;
    --grey-text: #8a8a8a;
    --nav-top: #5a5a5a;
    --nav-bottom: #262626;
    --panel-top: #fafafa;
    --panel-bottom: #e9e9e9;
    --panel-line: #d6d6d6;
    --white: #ffffff;
  }
  * { box-sizing: border-box; margin: 0; padding: 0; }
  html, body { width: 1200px; height: 850px; overflow: hidden; background: var(--white); }
  body { position: relative; font-family: "Open Sans", Arial, sans-serif; color: var(--ink); }

  .masthead { position: absolute; left: 0; top: 0; width: 1200px; height: 213px; overflow: hidden; }
  .masthead-backdrop {
    position: absolute; inset: 0;
    background: linear-gradient(90deg, #c8141c 0%, #e4606a 20%, #fbe6e7 38%, #ffffff 50%, #ececec 64%, #9a9a9a 84%, #111111 100%);
  }
  .brand { position: absolute; left: 344px; top: 52px; }
  .brand-name {
    display: flex; align-items: center; gap: 14px; white-space: nowrap;
    font-weight: 800; font-size: 38px; letter-spacing: -0.5px; color: var(--ink); line-height: 1;
  }
  .brand-mark { width: 60px; height: 60px; background: var(--red); flex: none; }
  .brand-slogan {
    margin: 8px 0 0 74px; font-size: 14px; font-weight: 700; color: var(--ink); white-space: nowrap;
  }

  .main-nav {
    position: absolute; left: 40px; top: 216px; width: 820px; height: 46px;
    background: linear-gradient(180deg, var(--nav-top), var(--nav-bottom));
    border-bottom: 3px solid #cfcfcf; border-radius: 3px 3px 0 0;
    display: flex; align-items: center; padding-left: 29px; gap: 15px;
  }
  .main-nav a { color: var(--white); text-decoration: none; font-size: 12.5px; text-transform: uppercase; }
  .main-nav a.is-current { color: #d8d8d8; }

  .slider {
    position: absolute; left: 40px; top: 313px; width: 820px; height: 336px;
    background: linear-gradient(100deg, #0b0e10 0%, #1c2a30 26%, #3b6a78 42%, #1c4452 60%, #0d2630 80%, #060a0c 100%);
  }
  .slider-arrow { position: absolute; top: 160px; width: 14px; height: 16px; background: #3a3a3a; }
  .slider-arrow.prev { left: 6px; }
  .slider-arrow.next { right: 6px; }
  .slider-arrow svg { display: block; }
  .slider-caption {
    position: absolute; left: 275px; top: 228px; width: 545px; height: 80px;
    background: rgba(20, 20, 20, 0.72); padding: 12px 0 0 11px; color: var(--white);
  }
  .slider-title { font-size: 30px; font-weight: 400; letter-spacing: -0.5px; line-height: 1.1; }
  .slider-sub { font-size: 12px; margin-top: 8px; text-transform: uppercase; }

  .feature-tiles { position: absolute; top: 658px; left: 40px; }
  .tile { position: absolute; top: 0; width: 181px; height: 173px; overflow: hidden; }
  .tile-image { position: absolute; inset: 0; }
  .tile-bar {
    position: absolute; left: 0; bottom: 0; width: 100%; height: 24px;
    background: rgba(30, 30, 30, 0.8); display: flex; justify-content: space-between; align-items: center;
  }
  .tile-label { color: var(--white); font-size: 11.5px; padding-left: 5px; text-transform: uppercase; }
  .tile-more {
    background: var(--red-deep); color: var(--white); font-size: 11.5px; height: 100%;
    display: flex; align-items: center; padding: 0 5px; text-transform: uppercase;
  }

  .sidebar { position: absolute; left: 892px; top: 216px; width: 288px; }
  .welcome-head {
    height: 46px; border-radius: 4px; background: linear-gradient(180deg, #5c5c5c, #222222);
    color: var(--white); font-weight: 700; font-size: 16px; text-align: center; line-height: 46px; letter-spacing: 0.5px;
  }
  .welcome-text {
    margin-top: 10px; font-size: 12.8px; line-height: 20px; color: var(--grey-text); text-align: justify; padding: 0 4px;
  }
  .contact-card {
    position: absolute; left: 0; width: 288px; height: 70px;
    background: linear-gradient(180deg, var(--panel-top), var(--panel-bottom));
    border: 1px solid var(--panel-line); display: flex; align-items: center; padding-left: 13px; gap: 18px;
  }
  .contact-icon { width: 38px; height: 38px; background: #2a2a2a; border-radius: 3px; flex: none; display: flex; align-items: center; justify-content: center; }
  .contact-title { color: var(--red-deep); font-weight: 700; font-size: 16px; line-height: 1.1; }
  .contact-note { color: #555; font-size: 11.5px; margin-top: 3px; }
</style>
</head>
<body>
  <header class="masthead">
    <div class="masthead-backdrop" role="img" aria-label="Decorative banner backdrop fading from red through white to black"></div>
    <div class="brand">
      <div class="brand-name"><span class="brand-mark"></span>BRIGHTLANE PARTNERS</div>
      <p class="brand-slogan">Providing Effective Project Controls and Management Solutions</p>
    </div>
  </header>

  <nav class="main-nav">
    <a class="is-current" href="#">Home</a>
    <a href="#">Services</a>
    <a href="#">Benefits</a>
    <a href="#">Management</a>
    <a href="#">Planning</a>
    <a href="#">Optimisation</a>
    <a href="#">Industry</a>
    <a href="#">Software</a>
    <a href="#">Contact us</a>
  </nav>

  <section class="slider" role="img" aria-label="Businessman holding a tablet beside a glass office tower with digital light squares">
    <span class="slider-arrow prev"><svg width="14" height="16" viewBox="0 0 14 16"><path d="M9 4 L5 8 L9 12 Z" fill="#bbb"/></svg></span>
    <span class="slider-arrow next"><svg width="14" height="16" viewBox="0 0 14 16"><path d="M5 4 L9 8 L5 12 Z" fill="#bbb"/></svg></span>
    <div class="slider-caption">
      <div class="slider-title">BRIGHTLANE PARTNERS</div>
      <div class="slider-sub">Knowledge | Expertise | Experience | Capacity</div>
    </div>
  </section>

  <div class="feature-tiles">
    <div class="tile" style="left:0">
      <div class="tile-image" role="img" aria-label="Group of business people standing in front of a world map" style="background:linear-gradient(180deg,#5aa6e6 0%,#bcdcf6 45%,#3a3f48 100%)"></div>
      <div class="tile-bar"><span class="tile-label">Services</span><span class="tile-more">Readmore»</span></div>
    </div>
    <div class="tile" style="left:210px">
      <div class="tile-image" role="img" aria-label="Coins, a calculator and financial charts on a desk" style="background:linear-gradient(160deg,#e9e4dc 0%,#b9a98a 40%,#6a6a6a 100%)"></div>
      <div class="tile-bar"><span class="tile-label">Benefits of</span><span class="tile-more">Readmore»</span></div>
    </div>
    <div class="tile" style="left:421px">
      <div class="tile-image" role="img" aria-label="Manager working at a desk in an office" style="background:linear-gradient(160deg,#d9d4cc 0%,#6f8fb2 50%,#3b4a5e 100%)"></div>
      <div class="tile-bar"><span class="tile-label">Management</span><span class="tile-more">Readmore»</span></div>
    </div>
    <div class="tile" style="left:631px">
      <div class="tile-image" role="img" aria-label="Hand writing on planning charts with a pen" style="background:linear-gradient(160deg,#f2f2f2 0%,#cfd6de 55%,#8d96a2 100%)"></div>
      <div class="tile-bar"><span class="tile-label">Planning</span><span class="tile-more">Readmore»</span></div>
    </div>
  </div>

  <aside class="sidebar">
    <h2 class="welcome-head">WELCOME</h2>
    <p class="welcome-text">Brightlane Partners provides effective project controls and management solutions to construction projects in Australia and Overseas. We provide services to both large multinational companies and smaller privately owned businesses. Our knowledge and expertise assist clients to effectively plan and manage their construction projects or project portfolios. Our focus is to provide your business with the tools, solutions and strategies necessary to deliver projects on time and within budget. We provide short or long term support, depending on your needs</p>

    <div class="contact-card" style="top:407px">
      <span class="contact-icon"><svg width="24" height="18" viewBox="0 0 24 18"><rect x="1" y="1" width="22" height="16" fill="none" stroke="#fff" stroke-width="2"/><path d="M1 1 L12 10 L23 1" fill="none" stroke="#fff" stroke-width="2"/></svg></span>
      <div><div class="contact-title">Email Us</div><div class="contact-note">Click here</div></div>
    </div>
    <div class="contact-card" style="top:490px">
      <span class="contact-icon"></span>
      <div><div class="contact-title">Circlepage</div><div class="contact-note">Follow us on</div></div>
    </div>
    <div class="contact-card" style="top:574px">
      <span class="contact-icon"></span>
      <div><div class="contact-title">Workline</div><div class="contact-note">Follow us on</div></div>
    </div>
  </aside>
</body>
</html>
```